Global Nano Technology Surface Protection company needs a new logo and cards

We are a Global company that will apply nanotechnology coatings on surfaces to prevent growth and spread of bacteria, viruses, mold etc. We deal with large corporates, airlines, hospitals and schools so we are after a new modern, simple and clean look that will have great visual impact.
We a company that is focused on prevention and protection.

Company name, Quorvane Systems Worldwide

Subtext, Antimicrobial Surface Protection

Logo, QVSW or QSW

Target Market(s)

Hospitals, Transport agencies, Airlines, Corporate entities

Industry/Entity Type

Protection

Contact Information for Business Card

Logo, QVSW or QSW
www.qvsw-example.us
Derek Holloway
+64290536218
tidyshieldnz@mailbox-example.com

Logo Text

QVSW

Requirements
Must have
• Simple clean look
Should not have
• Nothing too messy

```html
<!DOCTYPE html>
<html lang="en">
<head>
<meta charset="utf-8">
<title>Quorvane Systems Worldwide — Business Cards</title>
<link rel="stylesheet" href="https://fonts.googleapis.com/css2?family=Arimo:wght@400;700&display=swap">
<style>
  :root {
    --brand-blue: #05698f;
    --card-black: #1b1b1b;
    --swoosh-black: #1c1c1c;
    --text-white: #ffffff;
    --page-bg: #e4e4e4;
  }
  * { margin: 0; padding: 0; box-sizing: border-box; }
  html, body {
    width: 1200px;
    height: 1200px;
    overflow: hidden;
    background: var(--page-bg);
    font-family: "Arimo", Arial, sans-serif;
  }
  .canvas {
    position: relative;
    width: 1200px;
    height: 1200px;
  }
  .card {
    position: absolute;
    width: 735px;
    height: 420px;
    overflow: hidden;
  }
  .card-front {
    left: 168px;
    top: 169px;
    background: var(--brand-blue);
  }
  .card-back {
    left: 319px;
    top: 635px;
    background: var(--card-black);
  }
  .card-decor {
    position: absolute;
    inset: 0;
    width: 100%;
    height: 100%;
  }
  .front-brandmark {
    position: absolute;
    left: 0;
    right: 0;
    top: 140px;
    text-align: center;
    color: var(--text-white);
    font-weight: 700;
    font-size: 72px;
    letter-spacing: 2px;
    line-height: 1;
  }
  .front-website {
    position: absolute;
    left: 0;
    right: 0;
    top: 284px;
    text-align: center;
    color: var(--text-white);
    font-size: 31px;
    line-height: 1;
  }
  .back-brandmark {
    position: absolute;
    left: 40px;
    top: 164px;
    width: 200px;
    text-align: center;
    color: var(--brand-blue);
    font-weight: 700;
    font-size: 54px;
    letter-spacing: 1px;
    line-height: 1;
  }
  .company-name {
    position: absolute;
    left: 299px;
    top: 126px;
    color: var(--brand-blue);
    font-weight: 700;
    font-size: 20px;
    white-space: nowrap;
  }
  .company-tagline {
    position: absolute;
    left: 338px;
    top: 157px;
    color: var(--text-white);
    font-size: 19px;
    white-space: nowrap;
  }
  .contact-line {
    position: absolute;
    left: 335px;
    color: var(--text-white);
    font-size: 19px;
    white-space: nowrap;
    line-height: 1;
  }
  .contact-name { top: 218px; }
  .contact-phone { top: 250px; }
  .contact-web { top: 298px; left: 336px; }
  .contact-email { top: 330px; left: 336px; }
  .contact-icon {
    position: absolute;
    width: 22px;
    height: 22px;
  }
</style>
</head>
<body>
<main class="canvas">

  <section class="card card-front" aria-label="Business card front">
    <svg class="card-decor" viewBox="0 0 735 420" aria-hidden="true">
      <path d="M0 335 C50 332 100 316 130 290 C118 340 70 384 0 386 Z" fill="var(--swoosh-black)"/>
      <rect x="0" y="411" width="735" height="9" fill="var(--swoosh-black)"/>
    </svg>
    <div class="front-brandmark">QVSW</div>
    <div class="front-website">www.qvsw-example.us</div>
  </section>

  <section class="card card-back" aria-label="Business card back">
    <svg class="card-decor" viewBox="0 0 735 420" aria-hidden="true">
      <path d="M599 77 C630 40 680 20 735 22 L735 86 C690 70 640 68 599 77 Z" fill="var(--brand-blue)"/>
      <path d="M257 121 L259.5 211 L257 301 L254.5 211 Z" fill="var(--brand-blue)"/>
      <rect x="0" y="411" width="735" height="9" fill="var(--brand-blue)"/>
    </svg>

    <div class="back-brandmark">QVSW</div>

    <div class="company-name">Quorvane Systems Worldwide</div>
    <div class="company-tagline">Microbial Protection specialists</div>

    <div class="contact-line contact-name">Derek Holloway</div>

    <svg class="contact-icon" style="left:300px; top:249px;" viewBox="0 0 24 24" aria-hidden="true">
      <path d="M6.6 2.5 L9.5 6.8 L7.6 9 C8.6 11.5 10.6 14 13.5 15.8 L15.6 14 L20 16.8 L18.4 20.6 C11 21 3.5 13 3.2 5 Z" fill="var(--brand-blue)"/>
    </svg>
    <div class="contact-line contact-phone">+64290536218</div>

    <svg class="contact-icon" style="left:301px; top:296px;" viewBox="0 0 24 24" aria-hidden="true">
      <circle cx="12" cy="12" r="9" fill="none" stroke="var(--brand-blue)" stroke-width="2"/>
      <ellipse cx="12" cy="12" rx="4" ry="9" fill="none" stroke="var(--brand-blue)" stroke-width="1.6"/>
      <line x1="3" y1="12" x2="21" y2="12" stroke="var(--brand-blue)" stroke-width="1.6"/>
    </svg>
    <div class="contact-line contact-web">www.qvsw-example.us</div>

    <svg class="contact-icon" style="left:301px; top:328px;" viewBox="0 0 24 24" aria-hidden="true">
      <path d="M2 8 L12 2 L22 8 L22 21 L2 21 Z" fill="var(--brand-blue)"/>
      <path d="M2 9 L12 15 L22 9" fill="none" stroke="var(--card-black)" stroke-width="1.6"/>
    </svg>
    <div class="contact-line contact-email">tidyshieldnz@mailbox-example.com</div>
  </section>

</main>
</body>
</html>
```